Zielgruppe
Bei der Velkora Consulting GmbH handelt es sich um ein kürzlich in der Schweiz gegründetes Beratungsunternehmen im Projektmanagement und Change Management. Unser Serviceportfolio umfasst: Beratung, Training, Coaching und Interims-Management. Da Projektmanagement zu einem hohen Grad generisch ist, arbeiten wir branchenunabhängig. Derzeit sind wir in der Schweiz und Deutschland aktiv, aber es gibt auch Geschäftskontakte in andere Länder.
Aufgabenstellung
Ein Logo liegt bereits vor (siehe Dateiupload).
Folienformat 16:9 in PowerPoint 2013

```html
<!DOCTYPE html>
<html lang="de">
<head>
<meta charset="utf-8">
<title>Velkora Consulting – Präsentationsvorlage</title>
<link href="https://fonts.googleapis.com/css2?family=Questrial&display=swap" rel="stylesheet">
<style>
  :root{
    --brand-blue:#0a3a8c;
    --ink:#111;
    --grey:#a9a9a9;
    --grey-light:#d3d3d3;
    --rule:#dcdcdc;
    --paper:#fff;
    --photo-a:#9fc4cc;
    --photo-b:#2d7485;
  }
  html,body{margin:0;padding:0;overflow:hidden;}
  body{width:1200px;height:1200px;background:var(--paper);position:relative;font-family:"Questrial",sans-serif;}
  .slide{position:absolute;display:block;background:var(--paper);box-shadow:0 3px 8px rgba(0,0,0,.35);}
  .slide text{font-family:"Questrial",sans-serif;}
  .slide--title{left:371px;top:68px;width:482px;height:273px;}
  .slide--text{left:84px;top:394px;width:483px;height:272px;}
  .slide--ring{left:638px;top:394px;width:483px;height:272px;}
  .slide--bars{left:79px;top:719px;width:483px;height:272px;}
  .slide--photo{left:638px;top:719px;width:483px;height:272px;}
  .brand-mark{position:absolute;left:500px;top:1040px;width:200px;text-align:center;color:var(--brand-blue);}
  .brand-mark__dot{width:64px;height:64px;border-radius:50%;border:5px solid var(--brand-blue);margin:0 auto 14px;box-sizing:border-box;}
  .brand-mark__name{font-size:28px;line-height:1;white-space:nowrap;}
  .brand-mark__legal{font-size:16px;margin-top:6px;display:flex;align-items:center;gap:8px;justify-content:center;}
  .brand-mark__legal::before,.brand-mark__legal::after{content:"";width:44px;height:1px;background:var(--brand-blue);}
</style>
</head>
<body>

<!-- Titelfolie -->
<svg class="slide slide--title" viewBox="0 0 772 437" aria-label="Titelfolie">
  <rect width="772" height="437" fill="var(--brand-blue)"/>
  <path d="M0 0 A195 218.5 0 0 1 0 437 Z" fill="var(--paper)"/>
  <circle cx="100" cy="185" r="30" fill="none" stroke="var(--brand-blue)" stroke-width="5"/>
  <text x="100" y="248" font-size="24" fill="var(--brand-blue)" text-anchor="middle">Velkora</text>
  <text x="100" y="274" font-size="24" fill="var(--brand-blue)" text-anchor="middle">Consulting</text>
  <text x="100" y="296" font-size="13" fill="var(--brand-blue)" text-anchor="middle">GmbH</text>
  <text x="253" y="174" font-size="45" fill="#fff">Titel  der Präsentation</text>
  <text x="253" y="227" font-size="45" fill="#fff">zweizeilig</text>
  <text x="253" y="285" font-size="15" fill="#fff">PLATZHALTER UNTERTITEL</text>
</svg>

<!-- Textchart -->
<svg class="slide slide--text" viewBox="0 0 773 436" aria-label="Textchart">
  <path d="M16 0 V50 Q16 82 48 82 H773" fill="none" stroke="var(--brand-blue)" stroke-width="2.5"/>
  <text x="58" y="47" font-size="26" fill="var(--brand-blue)">Titel für ein Textchart 32 Punkt</text>
  <g fill="#888">
    <path d="M62 127 l11 7 -11 7z"/><path d="M62 162 l11 7 -11 7z"/><path d="M62 224 l11 7 -11 7z"/><path d="M62 314 l11 7 -11 7z"/>
  </g>
  <g font-size="22.5" fill="var(--ink)">
    <text x="82" y="141">Lorem ipsum dolor sit amet, consetetur sadipscing</text>
    <text x="82" y="176">elitr, sed diam nonumy eirmod tempor invidunt ut labore</text>
    <text x="82" y="203">et dolore magna aliquyam erat, sed diam voluptua.</text>
    <text x="82" y="238">At vero eos et accusam et justo duo dolores et ea</text>
    <text x="82" y="265">rebum. Stet clita kasd gubergren, no sea takimata</text>
    <text x="82" y="292">sanctus est</text>
    <text x="82" y="328">Lorem ipsum dolor sit amet. Lorem ipsum dolor sit amet,</text>
    <text x="82" y="355">consetetur</text>
  </g>
  <path d="M0 409 H745 Q758 409 758 422 V436" fill="none" stroke="var(--brand-blue)" stroke-width="2"/>
  <text x="526" y="426" font-size="8" fill="var(--brand-blue)">Dr. Lena Harbeck   Managing Partner</text>
  <circle cx="691" cy="423" r="7" fill="none" stroke="var(--grey)" stroke-width="1.5"/>
  <line x1="713" y1="415" x2="713" y2="431" stroke="var(--grey)"/>
  <text x="735" y="426" font-size="8" fill="var(--grey)">2</text>
</svg>

<!-- Textchart mit Ringgrafik -->
<svg class="slide slide--ring" viewBox="0 0 773 436" aria-label="Textchart mit Ringgrafik">
  <path d="M16 0 V50 Q16 82 48 82 H773" fill="none" stroke="var(--brand-blue)" stroke-width="2.5"/>
  <text x="58" y="47" font-size="26" fill="var(--brand-blue)">Titel für ein Textchart mit Ringgrafik 32 Punkt</text>
  <path d="M40 375 V155 Q40 115 80 115 H400" fill="none" stroke="var(--rule)" stroke-width="1.5"/>
  <g transform="rotate(-90 213 230)" fill="none" stroke-width="18">
    <circle cx="213" cy="230" r="73" stroke="var(--brand-blue)" stroke-dasharray="268.7 458.7"/>
    <circle cx="213" cy="230" r="73" stroke="var(--ink)" stroke-dasharray="104.9 458.7" stroke-dashoffset="-268.7"/>
    <circle cx="213" cy="230" r="73" stroke="var(--grey)" stroke-dasharray="45.9 458.7" stroke-dashoffset="-373.6"/>
    <circle cx="213" cy="230" r="73" stroke="var(--grey-light)" stroke-dasharray="39.4 458.7" stroke-dashoffset="-419.5"/>
  </g>
  <g font-size="8" fill="#fff">
    <text x="283" y="255">8,2</text><text x="133" y="258">3,2</text><text x="152" y="188">1,4</text><text x="188" y="166">1,2</text>
  </g>
  <g font-size="19" fill="var(--brand-blue)" text-anchor="middle">
    <text x="211" y="217">Umsätze</text><text x="213" y="241">2017</text><text x="213" y="265">In Mio €</text>
  </g>
  <g font-size="13" fill="var(--ink)">
    <rect x="52" y="341" width="5" height="5" fill="var(--brand-blue)"/><text x="60" y="351">1. Quartal</text>
    <rect x="138" y="341" width="5" height="5" fill="var(--ink)"/><text x="146" y="351">2. Quartal</text>
    <rect x="223" y="341" width="5" height="5" fill="var(--grey)"/><text x="231" y="351">3. Quartal</text>
    <rect x="308" y="341" width="5" height="5" fill="var(--grey-light)"/><text x="316" y="351">4. Quartal</text>
  </g>
  <g fill="#999"><path d="M430 116 l9 5 -9 5z"/><path d="M430 163 l9 5 -9 5z"/><path d="M430 249 l9 5 -9 5z"/><path d="M430 335 l9 5 -9 5z"/></g>
  <g font-size="16" fill="var(--ink)">
    <text x="451" y="127">Lorem ipsum dolor sit amet,</text><text x="451" y="146">consetetur sadipscing</text>
    <text x="451" y="174">elitr, sed diam nonumy eirmod</text><text x="451" y="193">tempor invidunt ut labore et dolore</text><text x="451" y="212">magna aliquyam erat, sed diam</text><text x="451" y="231">voluptua.</text>
    <text x="451" y="260">At vero eos et accusam et justo duo</text><text x="451" y="279">dolores et ea rebum. Stet clita kasd</text><text x="451" y="298">gubergren, no sea takimata sanctus</text><text x="451" y="317">est</text>
    <text x="451" y="346">Lorem ipsum dolor sit amet. Lorem</text><text x="451" y="365">ipsum dolor sit amet, consetetur</text>
  </g>
  <path d="M0 409 H745 Q758 409 758 422 V436" fill="none" stroke="var(--brand-blue)" stroke-width="2"/>
  <text x="526" y="426" font-size="8" fill="var(--brand-blue)">Dr. Lena Harbeck   Managing Partner</text>
  <circle cx="691" cy="423" r="7" fill="none" stroke="var(--grey)" stroke-width="1.5"/>
  <line x1="713" y1="415" x2="713" y2="431" stroke="var(--grey)"/>
  <text x="735" y="426" font-size="8" fill="var(--grey)">3</text>
</svg>

<!-- Textchart mit Säulengrafik -->
<svg class="slide slide--bars" viewBox="0 0 773 436" aria-label="Textchart mit Säulengrafik">
  <path d="M16 0 V50 Q16 82 48 82 H773" fill="none" stroke="var(--brand-blue)" stroke-width="2.5"/>
  <text x="58" y="47" font-size="26" fill="var(--brand-blue)">Titel für ein Textchart mit Säulengrafik 32 Punkt</text>
  <path d="M36 375 V155 Q36 115 76 115 H400" fill="none" stroke="var(--rule)" stroke-width="1.5"/>
  <rect x="68" y="154" width="43" height="176" fill="var(--brand-blue)"/>
  <rect x="156" y="262" width="43" height="68" fill="var(--ink)"/>
  <rect x="244" y="302" width="43" height="28" fill="var(--grey)"/>
  <rect x="332" y="306" width="43" height="24" fill="var(--grey-light)"/>
  <line x1="45" y1="331" x2="398" y2="331" stroke="var(--grey-light)"/>
  <g font-size="13" fill="var(--ink)" text-anchor="middle">
    <text x="90" y="353">1. Quartal</text><text x="178" y="353">2. Quartal</text><text x="266" y="353">3. Quartal</text><text x="354" y="353">4. Quartal</text>
  </g>
  <g font-size="19" fill="var(--brand-blue)" text-anchor="middle">
    <text x="263" y="179">Umsätze</text><text x="266" y="202">2017</text><text x="266" y="226">In Mio €</text>
  </g>
  <g fill="#999"><path d="M430 116 l9 5 -9 5z"/><path d="M430 163 l9 5 -9 5z"/><path d="M430 249 l9 5 -9 5z"/><path d="M430 335 l9 5 -9 5z"/></g>
  <g font-size="16" fill="var(--ink)">
    <text x="451" y="127">Lorem ipsum dolor sit amet,</text><text x="451" y="146">consetetur sadipscing</text>
    <text x="451" y="174">elitr, sed diam nonumy eirmod</text><text x="451" y="193">tempor invidunt ut labore et dolore</text><text x="451" y="212">magna aliquyam erat, sed diam</text><text x="451" y="231">voluptua.</text>
    <text x="451" y="260">At vero eos et accusam et justo duo</text><text x="451" y="279">dolores et ea rebum. Stet clita kasd</text><text x="451" y="298">gubergren, no sea takimata sanctus</text><text x="451" y="317">est</text>
    <text x="451" y="346">Lorem ipsum dolor sit amet. Lorem</text><text x="451" y="365">ipsum dolor sit amet, consetetur</text>
  </g>
  <path d="M0 409 H745 Q758 409 758 422 V436" fill="none" stroke="var(--brand-blue)" stroke-width="2"/>
  <text x="526" y="426" font-size="8" fill="var(--brand-blue)">Dr. Lena Harbeck   Managing Partner</text>
  <circle cx="691" cy="423" r="7" fill="none" stroke="var(--grey)" stroke-width="1.5"/>
  <line x1="713" y1="415" x2="713" y2="431" stroke="var(--grey)"/>
  <text x="735" y="426" font-size="8" fill="var(--grey)">4</text>
</svg>

<!-- Textchart mit Bild -->
<svg class="slide slide--photo" viewBox="0 0 773 436" aria-label="Textchart mit Bild">
  <defs>
    <linearGradient id="photoTone" x1="0" y1="0" x2="1" y2="1">
      <stop offset="0" stop-color="var(--photo-a)"/><stop offset="1" stop-color="var(--photo-b)"/>
    </linearGradient>
  </defs>
  <path d="M16 0 V50 Q16 82 48 82 H773" fill="none" stroke="var(--brand-blue)" stroke-width="2.5"/>
  <text x="58" y="47" font-size="26" fill="var(--brand-blue)">Titel für ein Textchart mit Bild 32 Punkt</text>
  <path d="M37 375 V150 Q37 115 72 115 H400 V340 Q400 375 365 375 Z" fill="url(#photoTone)" role="img" aria-label="Foto: Geschäftsfrau tippt auf ein Tablet vor einem leuchtenden Netzwerk mit dem Wort RISK"/>
  <g fill="#999"><path d="M430 116 l9 5 -9 5z"/><path d="M430 163 l9 5 -9 5z"/><path d="M430 249 l9 5 -9 5z"/><path d="M430 335 l9 5 -9 5z"/></g>
  <g font-size="16" fill="var(--ink)">
    <text x="451" y="127">Lorem ipsum dolor sit amet,</text><text x="451" y="146">consetetur sadipscing</text>
    <text x="451" y="174">elitr, sed diam nonumy eirmod</text><text x="451" y="193">tempor invidunt ut labore et dolore</text><text x="451" y="212">magna aliquyam erat, sed diam</text><text x="451" y="231">voluptua.</text>
    <text x="451" y="260">At vero eos et accusam et justo duo</text><text x="451" y="279">dolores et ea rebum. Stet clita kasd</text><text x="451" y="298">gubergren, no sea takimata sanctus</text><text x="451" y="317">est</text>
    <text x="451" y="346">Lorem ipsum dolor sit amet. Lorem</text><text x="451" y="365">ipsum dolor sit amet, consetetur</text>
  </g>
  <path d="M0 409 H745 Q758 409 758 422 V436" fill="none" stroke="var(--brand-blue)" stroke-width="2"/>
  <text x="526" y="426" font-size="8" fill="var(--brand-blue)">Dr. Lena Harbeck   Managing Partner</text>
  <circle cx="691" cy="423" r="7" fill="none" stroke="var(--grey)" stroke-width="1.5"/>
  <line x1="713" y1="415" x2="713" y2="431" stroke="var(--grey)"/>
  <text x="735" y="426" font-size="8" fill="var(--grey)">5</text>
</svg>

<!-- Firmenname -->
<div class="brand-mark">
  <div class="brand-mark__dot"></div>
  <div class="brand-mark__name">Velkora Consulting</div>
  <div class="brand-mark__legal">GmbH</div>
</div>

</body>
</html>
```